Pretzel Company needs a Pretzel Bag Design for Retail

Benny Twists, a smoked, seasoned pretzel maker, needs an eye popping pretzel package design that will make consumers excited to try their smoked, seasoned pretzels

```html
<!DOCTYPE html>
<html lang="en">
<head>
<meta charset="utf-8">
<title>Benny Twists – Pretzel Bag Design</title>
<link href="https://fonts.googleapis.com/css2?family=Archivo:wght@400;700;900&family=Source+Sans+3:ital,wght@0,400;0,600;0,700;1,700&display=swap" rel="stylesheet">
<style>
  :root{
    --bag-yellow:#ffff00;
    --bag-orange:#fcc51f;
    --bag-purple:#662f90;
    --bag-plum:#5f006a;
    --ink:#111111;
    --paper:#ffffff;
    --window-a:#d9d3d6;
    --window-b:#a8a0a6;
  }
  *{box-sizing:border-box;margin:0;padding:0}
  html,body{width:1200px;height:1200px;overflow:hidden;background:var(--paper)}
  body{position:relative;font-family:"Source Sans 3",Arial,sans-serif;color:var(--ink)}

  .side-label{position:absolute;font-family:"Source Sans 3",Arial,sans-serif;font-weight:700;font-style:italic;font-size:38px;line-height:1;color:var(--ink)}
  .side-label--front{left:122px;top:146px}
  .side-label--back{left:628px;top:152px}

  .bag-panel{position:absolute;top:207px;width:453px;height:744px;overflow:hidden;box-shadow:0 14px 12px -10px rgba(0,0,0,.35)}
  .bag-panel--front{left:116px}
  .bag-panel--back{left:617px}
  .panel-art{position:absolute;inset:0;width:453px;height:744px;display:block}

  .brand-seal{position:absolute;border:3px solid var(--paper);border-radius:50%;display:flex;align-items:center;justify-content:center}
  .brand-seal--front{left:111px;top:88px;width:220px;height:220px}
  .brand-seal--back{left:52px;top:82px;width:116px;height:116px;border-width:2px}
  .brand-name{font-family:"Source Sans 3",Arial,sans-serif;font-weight:700;color:var(--paper);text-align:center;line-height:.95}
  .brand-seal--front .brand-name{font-size:44px}
  .brand-seal--back .brand-name{font-size:23px}

  .product-window{position:absolute;left:98px;top:458px;width:262px;height:196px;border-radius:50%;background:radial-gradient(ellipse at 45% 40%,var(--window-a),var(--window-b))}

  .front-tagline{position:absolute;left:39px;top:677px;font-weight:700;font-style:italic;font-size:14px}
  .weight-badge{position:absolute;left:349px;top:654px;width:58px;height:58px;border-radius:50%;background:var(--ink);color:var(--paper);font-family:"Archivo",Arial,sans-serif;font-weight:700;font-size:19px;display:flex;align-items:center;justify-content:center}

  .back-copy{position:absolute;font-size:11px;line-height:14.5px}
  .back-copy--top{left:211px;top:79px;width:200px;color:var(--paper)}
  .back-copy--side{left:310px;top:333px;width:118px;color:var(--bag-purple);font-size:11.3px}

  .nutrition-label{position:absolute;left:53px;top:288px;width:196px;height:332px;border:1px solid var(--ink);padding:2px 3px;font-family:"Archivo",Arial,sans-serif;font-size:7.4px;line-height:1.15;color:var(--ink)}
  .nf-title{font-weight:900;font-size:21px;line-height:1;letter-spacing:-.2px;border-bottom:1px solid var(--ink);padding-bottom:1px}
  .nf-servings{font-size:9px;padding-top:2px}
  .nf-size{display:flex;justify-content:space-between;font-weight:900;font-size:10px;padding-bottom:2px;border-bottom:7px solid var(--ink)}
  .nf-amount{font-weight:700;font-size:5.5px;padding-top:2px}
  .nf-cal{display:flex;justify-content:space-between;align-items:flex-end;font-weight:900;font-size:16px;line-height:1;border-bottom:4px solid var(--ink);padding-bottom:1px}
  .nf-cal .nf-cal-value{font-size:25px}
  .nf-dv-head{text-align:right;font-weight:700;font-size:5.5px;border-bottom:1px solid var(--ink);padding:1px 0}
  .nf-row{display:flex;justify-content:space-between;border-bottom:1px solid var(--ink);padding:2px 0 1px}
  .nf-row b{font-weight:900}
  .nf-row .nf-pct{font-weight:900}
  .nf-row--sub{padding-left:10px}
  .nf-row--subsub{padding-left:20px}
  .nf-row--protein{border-bottom:7px solid var(--ink)}
  .nf-row--mineral .nf-pct{font-weight:400}
  .nf-row--last{border-bottom:3px solid var(--ink)}
  .nf-foot{font-size:5.4px;line-height:1.3;padding:2px 0 0 4px}

  .ingredients{position:absolute;left:53px;top:630px;width:232px;font-family:"Archivo",Arial,sans-serif;font-size:5.7px;line-height:1.4}
  .ingredients b{font-weight:700}
</style>
</head>
<body>

<h2 class="side-label side-label--front">Front</h2>
<h2 class="side-label side-label--back">Back</h2>

<section class="bag-panel bag-panel--front">
  <svg class="panel-art" viewBox="0 0 453 744" aria-hidden="true">
    <rect width="453" height="744" fill="var(--bag-yellow)"/>
    <path d="M0,340 C150,395 300,425 350,433 C230,445 160,470 170,520 C180,600 330,640 453,650 L453,744 L0,744 Z" fill="var(--bag-orange)"/>
    <path d="M0,75 C60,12 180,8 260,32 C340,56 400,22 430,0 L453,0 L453,265 C380,330 300,370 240,370 C150,370 60,345 0,333 Z" fill="var(--bag-purple)"/>
    <path d="M60,290 C170,170 330,110 453,140 L453,265 C380,330 300,370 240,370 C160,370 90,350 40,340 Z" fill="var(--bag-plum)"/>
  </svg>
  <div class="brand-seal brand-seal--front"><p class="brand-name">Benny<br>Twists</p></div>
  <div class="product-window" role="img" aria-label="Clear window showing the colourful seasoned pretzel pieces inside the bag"></div>
  <p class="front-tagline">Lorem ipsum dolor sit amet,</p>
  <div class="weight-badge">000g</div>
</section>

<section class="bag-panel bag-panel--back">
  <svg class="panel-art" viewBox="0 0 453 744" aria-hidden="true">
    <rect width="453" height="744" fill="var(--bag-yellow)"/>
    <path d="M0,268 C30,300 50,400 42,550 C36,650 40,700 48,744 L0,744 Z" fill="var(--bag-orange)"/>
    <path d="M453,598 C410,640 378,700 388,744 L453,744 Z" fill="var(--bag-orange)"/>
    <path d="M0,0 L453,0 L453,318 C400,320 330,305 250,270 C150,228 80,220 0,265 Z" fill="var(--bag-purple)"/>
  </svg>
  <div class="brand-seal brand-seal--back"><p class="brand-name">Benny<br>Twists</p></div>
  <p class="back-copy back-copy--top">Lorem ipsum dolor sit amet, consectetuer adipiscing elit, sed diam nonummy nibh euismod tincidunt ut laoreet dolore magna aliquam erat volutpat. Ut wisi enim ad minim veniam, quis nostrud exerci tation ullamcorper suscipit lobortis nisl ut aliquip ex ea commodo consequat. Duis autem vel eum iriure dolor in hendrerit in vulpu</p>

  <div class="nutrition-label">
    <div class="nf-title">Nutrition Facts</div>
    <div class="nf-servings">12 servings per container</div>
    <div class="nf-size"><span>Serving size</span><span>15 pretzels (28g)</span></div>
    <div class="nf-amount">Amount per serving</div>
    <div class="nf-cal"><span>Calories</span><span class="nf-cal-value">130</span></div>
    <div class="nf-dv-head">% Daily Value*</div>
    <div class="nf-row"><span><b>Total Fat</b> 7g</span><span class="nf-pct">9%</span></div>
    <div class="nf-row nf-row--sub"><span>Saturated Fat 1g</span><span class="nf-pct">4%</span></div>
    <div class="nf-row nf-row--sub"><span><i>Trans</i> Fat 0g</span><span></span></div>
    <div class="nf-row"><span><b>Cholesterol</b> 0mg</span><span class="nf-pct">0%</span></div>
    <div class="nf-row"><span><b>Sodium</b> 350mg</span><span class="nf-pct">15%</span></div>
    <div class="nf-row"><span><b>Total Carbohydrate</b> 17g</span><span class="nf-pct">6%</span></div>
    <div class="nf-row nf-row--sub"><span>Dietary Fiber 0g</span><span class="nf-pct">0%</span></div>
    <div class="nf-row nf-row--sub"><span>Total Sugars 0g</span><span></span></div>
    <div class="nf-row nf-row--subsub"><span>Includes 0g Added Sugars</span><span class="nf-pct">0%</span></div>
    <div class="nf-row nf-row--protein"><span><b>Protein</b> 2g</span><span></span></div>
    <div class="nf-row nf-row--mineral"><span>Vitamin D 0mcg</span><span class="nf-pct">0%</span></div>
    <div class="nf-row nf-row--mineral"><span>Calcium 0mg</span><span class="nf-pct">0%</span></div>
    <div class="nf-row nf-row--mineral"><span>Iron 1mg</span><span class="nf-pct">4%</span></div>
    <div class="nf-row nf-row--mineral nf-row--last"><span>Potassium 0mg</span><span class="nf-pct">0%</span></div>
    <p class="nf-foot">* The % Daily Value (DV) tells you how much a nutrient in a serving of food contributes to a daily diet. 2,000 calories a day is used for general nutrition advice.</p>
  </div>

  <p class="ingredients"><b>INGREDIENTS:</b> Pretzels (Wheat Flour, Salt, Vegetable Oil [Corn, Sunflower or Canola], Malt Syrup [Derived from Corn and Malted Barley], Yeast, Baking Soda); Soybean Oil, Artificial Flavor, Beta Carotene (for Color); Seasoning (Maltodextrin, Buttermilk, Salt, Monosodium Glutamate, Garlic, Onion, Lactic Acid, Calcium Lactate, Citric Acid, Garlic, Paprika, Chili Pepper, Less Than 2% of Vinegar, Red Bell Pepper, Calcium Silicate, Artificial Flavor, Xanthan Gum, Carboxymethylcellulose, Guar Gum, Natural Flavor); Cayenne Pepper, Silicon Dioxide (to Prevent Caking).<br><b>CONTAINS: WHEAT, SOY, MILK.</b></p>

  <p class="back-copy back-copy--side">Lorem ipsum dolor sit amet, consectetuer adipiscing elit, sed diam nonummy nibh euismod tincidunt ut laoreet dolore magna aliquam erat volutpat. Ut wisi enim ad minim veniam, quis nostrud exerci tation ullamcorper suscipit lobortis nisl ut aliquip ex ea commodo consequat. Duis autem vel eum iriure dolor in hendrerit in vulputate velit esse molestie consequat, vel illum dolore eu feugiat nulla facilisis at vero eros et</p>
</section>

</body>
</html>
```